Business card design needed

I have a small café in a small coastal town on the Central coast of NSW (Aus) I need something simple but noticeable. My café is on the main rd and while there is a lot of passing traffic I need a logo which will make people notice us, either through pamphlets or signage. We make almost everything freshly on the premises including cakes, burgers, hot chips, coffees and milkshakes. we also sell some cake decorating supplies. I am pretty open to designs and don't mind if these items are incorporated in the design. My frontage is aqua and my outdoor furniture is beige. Inside we have a small amount of aqua and the walls are white. I am happy for any variations of these colours or anything which goes with the aqua.

Contact Information for Business Card

Reed & Lantern Café
127 Harrow Rd West Bindell
02 48 61 2593
Open for breakfast and lunch
from 6am Monday - Saturday

```html
<!DOCTYPE html>
<html lang="en">
<head>
<meta charset="utf-8">
<title>Reed &amp; Lantern Café – Business Card</title>
<link rel="stylesheet" href="https://fonts.googleapis.com/css2?family=Quicksand:wght@400;500;700&display=swap">
<style>
  :root {
    --stage: #2b2c2e;
    --card-top: #ffffff;
    --card-bottom: #d6f2f4;
    --icing-pink: #f21ba8;
    --icing-pink-soft: #f77fcb;
    --aqua: #3ecbdc;
    --aqua-deep: #1fb2c6;
    --info-teal: #27b59a;
    --cream: #fffbee;
  }
  * { box-sizing: border-box; margin: 0; padding: 0; }
  html, body {
    width: 1200px;
    height: 1000px;
    overflow: hidden;
  }
  body {
    background: var(--stage);
    font-family: "Quicksand", sans-serif;
    position: relative;
  }
  .business-card {
    position: absolute;
    left: 100px;
    top: 200px;
    width: 1000px;
    height: 600px;
    background:
      radial-gradient(ellipse 70% 55% at 50% 40%, rgba(255,255,255,0.9), rgba(255,255,255,0) 70%),
      linear-gradient(180deg, var(--card-top) 0%, var(--card-bottom) 100%);
    overflow: hidden;
    box-shadow: 0 18px 40px rgba(0,0,0,0.45);
  }
  .icing-band {
    position: absolute;
    left: 0; top: 0;
    width: 100%;
    height: 44px;
    background: var(--icing-pink);
  }
  .icing-drips {
    position: absolute;
    left: 0; top: 44px;
    width: 100%;
    height: 170px;
    background: linear-gradient(180deg, var(--icing-pink-soft) 0%, rgba(247,127,203,0.35) 45%, rgba(190,238,244,0.55) 75%, rgba(255,255,255,0) 100%);
  }
  .brand-name {
    position: absolute;
    left: 0; right: 0;
    top: 250px;
    display: flex;
    align-items: center;
    justify-content: center;
    gap: 22px;
    font-weight: 700;
    font-size: 84px;
    line-height: 1;
    color: var(--aqua);
  }
  .brand-dot {
    width: 26px;
    height: 26px;
    border-radius: 50%;
    background: var(--icing-pink);
    flex: none;
  }
  .contact-details {
    position: absolute;
    left: 0; right: 0;
    top: 392px;
    text-align: center;
    font-weight: 500;
    font-size: 28px;
    line-height: 1.4;
    color: var(--info-teal);
  }
</style>
</head>
<body>
  <article class="business-card">
    <div class="icing-band"></div>
    <div class="icing-drips" role="img" aria-label="Pink icing dripping down over a pale aqua background"></div>

    <h1 class="brand-name">
      <span>Reed &amp; Lantern Café</span>
      <span class="brand-dot" aria-hidden="true"></span>
    </h1>

    <div class="contact-details">
      <p class="contact-address">127 Harrow Rd West Bindell 02 48 61 2593</p>
      <p class="contact-hours">Open for breakfast and lunch from 6am Monday - Saturday</p>
    </div>
  </article>
</body>
</html>
```